Website for new academic journal of deconstruction and psychoanalysis

- This project has been put on hold because of a mistake I made. I requested that the project be for a journal cover and matching website. The problem was that I was trying to get web designers to design a book cover first, and it was not working. I have started a new project for a book or journal cover. Once that project has been completed, I will bring the book cover design over to this project so that it can be used with the website design. This way this design project can focus on the function of the website. -

The function of the website will be similar to the function of these other KRB journals. I give you these other journals just as examples of journal websites and journal covers:

http://www.qvrm.dalbrook.ac.uk/
http://archive.fenwold.edu/
http://www.gmt.halvercrest.edu/~vostrine/
http://www.tamberlyreview.org/subscribe/subscribe-to-tamberly/

The MV website will have the following buttons/pages:

Home
About the Journal
Issues
News and Events
Blog
Submissions
Contact
Links
Updates

- This project has been put on hold because of a mistake I made.  I requested that the project be for a journal cover and matching website.  The problem was that I was trying to get web designers to design a book cover first, and it was not working.  I have started a new project for a book or journal cover.  Once that project has been completed, I will bring the book cover design over to this project so that it can be used with the website design.  This way this design project can focus on the function of the website. -

Target Market(s)

Professional academics and psychoanalytic clinicians.

Industry/Entity Type

Events

Font styles to use
Sans Serif

Requirements
Nice to have
• A very contemporary feel. Simplicity. Bold colors.
Should not have
• NO photos of Hallam or Lemoyne, or photos of anyone. No photos of books or academic icons.

```html
<!DOCTYPE html>
<html lang="en">
<head>
<meta charset="utf-8">
<title>The Unresolved Interior – Writings on Theory and the Clinic</title>
<link rel="stylesheet" href="https://fonts.googleapis.com/css2?family=Pathway+Gothic+One&family=Raleway:wght@400;600;700&family=Roboto+Condensed:wght@700&display=swap">
<style>
:root{
  --pink:#e8388f;
  --pink-deep:#c8136b;
  --orange:#f39200;
  --orange-dark:#e38e0f;
  --ink:#333;
  --muted:#777;
  --rule:#dcdcdc;
  --white:#fff;
}
*{box-sizing:border-box;margin:0;padding:0}
html,body{width:1120px;height:1200px;overflow:hidden;background:var(--white)}
body{font-family:"Raleway",sans-serif;color:var(--ink);font-size:11.5px;line-height:19.2px;position:relative}
a{color:inherit;text-decoration:none}

.site-header{height:83px;position:relative}
.brand{position:absolute;left:170px;top:17px}
.brand-name{display:flex;align-items:center;gap:10px;font-family:"Raleway",sans-serif;font-weight:700;font-size:27px;line-height:32px;color:var(--pink)}
.brand-name .mark{width:14px;height:14px;background:var(--pink)}
.brand-tagline{font-family:"Raleway",sans-serif;font-size:13px;line-height:20px;color:var(--orange);margin:4px 0 0 24px}
.search{position:absolute;left:742px;top:27px;width:200px;height:30px;border:1px solid #ddd;display:flex}
.search span{flex:1;padding:5px 8px;font-size:11.5px;color:#555}
.search .search-btn{width:30px;border-left:1px solid #ddd;display:flex;align-items:center;justify-content:center}

.main-nav{height:44px;border-top:1px solid var(--rule);border-bottom:1px solid var(--rule);position:relative}
.main-nav ul{list-style:none;display:flex;position:absolute;left:160px;top:-1px}
.main-nav li{width:100px;height:45px;border-right:1px solid var(--rule);display:flex;align-items:center;justify-content:center;font-family:"Roboto Condensed",sans-serif;font-weight:700;font-size:11.5px;color:#222}
.main-nav li.active{background:var(--orange);color:var(--white)}

.hero{height:337px;background:linear-gradient(90deg,var(--orange),var(--orange-dark));position:relative}
.cover{position:absolute;left:172px;top:23px;width:221px;height:294px;background:var(--white);padding:4px}
.cover div{width:100%;height:100%;background:linear-gradient(180deg,#c0136f,#a50f5a 60%,#5a0b2f)}
.about{position:absolute;left:409px;top:22px;width:296px;color:var(--white)}
.about h2{font-family:"Pathway Gothic One",sans-serif;font-weight:400;font-size:46px;line-height:50px;color:var(--pink-deep);margin-bottom:4px}
.about h3{font-size:11.5px;font-weight:700}
.about p+p{margin-top:19px}
.know-more{color:var(--pink-deep);font-weight:700}
.editors{position:absolute;left:722px;top:62px;width:230px;height:253px;border-left:1px solid rgba(255,255,255,.25);padding-left:26px;color:var(--white)}
.editors dl div{padding:2px 0 8px;border-bottom:1px solid rgba(255,255,255,.35);margin-bottom:11px;width:180px}
.editors dl div:nth-child(2){width:200px}
.editors dl div:last-child{border:none;width:200px}
.editors dt{font-weight:700}

.content{position:absolute;left:172px;top:488px;width:520px}
.post{border-bottom:1px solid var(--rule);padding-bottom:10px;margin-bottom:14px}
.post h2{font-size:29px;line-height:32px;font-weight:600;color:var(--pink)}
.post .meta{color:var(--muted);margin-bottom:10px}
.thumb{width:101px;height:77px;border:1px solid #ccc;padding:3px;background:#fff}
.thumb div{width:100%;height:100%;background:linear-gradient(135deg,#f0f0f0,#c9c9c9)}
.post-one .thumb{float:left;margin:0 9px 12px 1px}
.post-two .thumb{float:right;width:217px;height:150px;margin:0 1px 12px 12px}
.post-two .thumb div{background:linear-gradient(180deg,#eef0f4,#d8dce6)}
.post-one p.lead{margin-bottom:12px}
.post-one p.rest{clear:both;margin-left:2px}
.post-two{padding-bottom:6px}

.news{position:absolute;left:724px;top:502px;width:218px;border:1px solid #ccc;box-shadow:0 1px 3px rgba(0,0,0,.15);background:linear-gradient(180deg,#f2f2f2,#fff 60px)}
.news h2{font-size:19px;line-height:22px;font-weight:600;color:var(--orange);padding:10px 10px 4px}
.news article{padding:0 7px 6px 12px;border-bottom:1px solid #ccc;margin-bottom:8px}
.news article h3{font-size:12.5px;line-height:14px;font-weight:600;color:#222;margin:4px 0 6px}
.news time{color:var(--muted);display:block}
.news .more{color:var(--pink)}
.news .all{text-align:center;padding:0 0 10px;margin-top:-2px}
.news .all a{color:var(--pink);font-weight:700;text-decoration:underline}

.site-footer{position:absolute;left:0;top:1139px;width:1120px;height:61px;background:var(--orange);border-top:2px solid #e0e0e0;color:var(--white);font-size:11.5px;padding:22px 0 0 173px}
</style>
</head>
<body>
<header class="site-header">
  <div class="brand">
    <div class="brand-name"><span class="mark"></span>The Unresolved Interior</div>
    <div class="brand-tagline">Writings on Theory and the Clinic</div>
  </div>
  <div class="search">
    <span>Search</span>
    <div class="search-btn"><svg width="11" height="11" viewBox="0 0 11 11"><circle cx="4.5" cy="4.5" r="3.2" fill="none" stroke="#e8388f" stroke-width="1.8"/><line x1="7" y1="7" x2="10" y2="10" stroke="#e8388f" stroke-width="2"/></svg></div>
  </div>
</header>

<nav class="main-nav">
  <ul>
    <li class="active">Home</li><li>About the Journal</li><li>Issues</li><li>News and Events</li><li>Blog</li><li>Submissions</li><li>Contact</li><li>Links</li>
  </ul>
</nav>

<section class="hero">
  <figure class="cover"><div role="img" aria-label="Journal cover artwork, Volume 1, Issue 1, 2014"></div></figure>
  <div class="about">
    <h2>ABOUT THE JOURNAL</h2>
    <h3>Introducton:</h3>
    <p>Pellentesque habitant morbi tristique senectus et netus et malesuada fames ac turpis egestas. Nulla nulla nulla, pharetra lacinia odio sed, egestas laoreet ipsum. Nulla dictum lobortis elit eu laoreet. Vestibulum posuere, eros id vestibulum tincidunt.</p>
    <p>Sed viverra condimentum tincidunt. Sed ut ornare ante, id pellentesque magna. Curabitur facilisis nulla venenatis, adipiscing odio sed, fermentum erat. Morbi auctor, mi in ultrices tincidunt, est augue lacinia lectus<br><a class="know-more" href="#">Know More ›</a></p>
  </div>
  <aside class="editors">
    <dl>
      <div><dt>General Editor</dt><dd>James Wexley(Sollicitudin Ipsum University)</dd></div>
      <div><dt>Assistant Editor</dt><dd>Keith Tolland (Univ. of Harrowby)</dd></div>
      <div><dt>Editorial Board</dt><dd>Frank Wendell, Mike Sorrel, Steve Gilmont, Ron Haskin, Bret Tamsin, Gale Swinton</dd></div>
    </dl>
  </aside>
</section>

<main class="content">
  <article class="post post-one">
    <h2>Aenean posuere velit a erat</h2>
    <p class="meta">Posted by admin in Issues on November 9, 2013</p>
    <figure class="thumb"><div role="img" aria-label="Illustration of a bar chart under a magnifying glass"></div></figure>
    <p class="lead">Vestibulum lacinia congue commodo. Sed lorem erat, euismod at risus at, sollicitudin venenatis risus. Praesent cursus lacus ac eros feugiat, vitae eleifend felis hendrerit. In hac habitasse platea dictumst. Nullam convallis mauris quis hendrerit accumsan. Sed auctor tempor neque quis ultricies.</p>
    <p class="rest">Nulla suscipit semper volutpat. Sed ullamcorper enim quis dolor pellentesque dictum. Integer convallis, massa tincidunt laoreet auctor, mi ante pretium lacus, ac congue odio ante non nunc. Class aptent taciti sociosqu ad litora torquent per conubia nostra, per inceptos himenaeos. Praesent cursus lacus ac eros feugiat, vitae eleifend felis hendrerit. In hac habitasse platea dictumst. Nullam convallis mauris quis hendrerit accumsan. Sed auctor tempor neque quis ultricies.</p>
  </article>
  <article class="post post-two">
    <h2>Pellentesque habitant morbi tristique</h2>
    <p class="meta">Posted by admin in Issues on November 8, 2013</p>
    <figure class="thumb"><div role="img" aria-label="Statistics chart image with coloured bars"></div></figure>
    <p>Nulla suscipit semper volutpat. Sed ullamcorper enim quis dolor pellentesque dictum. Integer convallis, massa tincidunt laoreet auctor, mi ante pretium lacus, ac congue odio ante non nunc. Class aptent taciti sociosqu ad litora torquent per conubia nostra, per inceptos himenaeos. Praesent cursus lacus ac eros feugiat, vitae eleifend felis hendrerit. In hac habitasse platea dictumst. Nullam convallis mauris quis hendrerit accumsan. Sed laoreet auctor, mi ante pretium lacus, ac congue odio ante non nunc. Class aptent taciti sociosqu ad litora torquent per conubia nostra, per inceptos himenaeos. Praesent cursus lacus ac eros feugiat, vitae eleifend felis hendrerit. In hac habitasse platea dictumst. Nullam convallis mauris quis hendrerit accumsan. Sed. Sed ut ornare ante, id pellentesque magna. Curabitur facilisis nulla venenatis, adipiscing odio sed, fermentum erat. Morbi auctor, mi in ultrices tincidunt, est augue lacinia lectus, nec auctor arcu tellus nec nisi.</p>
  </article>
</main>

<aside class="news">
  <h2>NEWS &amp; EVENTS</h2>
  <article>
    <h3>Vestibulum lacinia congue commodo</h3>
    <time>November 10, 2013</time>
    <p>Sed ullamcorper enim quis dolor pellentesque dictum. Integer convallis, massa tincidunt laoreet auctor, mi ante pretium lacus, ac congue odio ante non nunc...</p>
    <a class="more" href="#">Read More ›</a>
  </article>
  <article>
    <h3>Praesent cursus lacus ac eros</h3>
    <time>November 9, 2013</time>
    <p>Sed ullamcorper enim quis dolor pellentesque dictum. Integer convallis, massa tincidunt laoreet auctor, mi ante pretium lacus, ac congue odio ante non nunc...</p>
    <a class="more" href="#">Read More ›</a>
  </article>
  <article>
    <h3>Nullam convallis mauris quis</h3>
    <time>November 8, 2013</time>
    <p>Vestibulum posuere, eros id vestibulum tincidunt, mi dolor elementum magna, non porta orci justo sit amet justo. Sed viverra condimentum tincidunt...</p>
    <a class="more" href="#">Read More ›</a>
  </article>
  <div class="all"><a href="#">Click here to Read All News</a></div>
</aside>

<footer class="site-footer">Copyright © 2013 The Unresolved Interior. All rights resered</footer>
</body>
</html>
```